Silver Brook Constructions Ltd Stationary
business cards, stationary etc.
Silver Brook Constructions Ltd Stationary - Construction
Creative Brief
Simple
Dalton Wexford
4816 Ardmore Rd. Victoria B.C. V8N 4K7
250-384-6252 could we put this number under office instead of phone
222-222-2222 temporary until I get new number
dalton@silverbrookconstructions.example
www.silverbrookconstructions.example
We would like designs for business cards , envelopes, letterhead, thank-you cards with evelopes, fax cover sheet, and presentation folder. Thank you
information should be on the back of the card along with some clean lines and simplicity while keeping a very professional feel

```html
<!DOCTYPE html>
<html lang="en">
<head>
<meta charset="utf-8">
<title>Silver Brook Constructions Ltd – Business Card</title>
<link rel="stylesheet" href="https://fonts.googleapis.com/css2?family=Cinzel:wght@400;600&family=Crimson+Text:wght@400&display=swap">
<style>
  :root {
    --backdrop: #e9e6e1;
    --card: #ffffff;
    --ink: #3b3b3b;
    --muted: #6b6b6b;
    --leaf: #6e8f3a;
  }
  * { margin: 0; padding: 0; box-sizing: border-box; }
  html, body { width: 1200px; height: 852px; overflow: hidden; }
  body {
    background: var(--backdrop);
    display: flex;
    align-items: center;
    justify-content: center;
    gap: 40px;
  }
  .card {
    position: relative;
    width: 520px;
    height: 297px;
    background: var(--card);
    border-radius: 14px;
    box-shadow: 0 6px 18px rgba(0,0,0,0.12);
    overflow: hidden;
  }
  /* front */
  .card--front { text-align: center; }
  .brand-name {
    position: absolute;
    left: 0; right: 0; top: 112px;
    font-family: "Cinzel", serif;
    font-weight: 600;
    color: var(--ink);
    line-height: 1;
  }
  .brand-name__main { display: block; font-size: 34px; letter-spacing: 1px; }
  .brand-name__sub { display: block; font-size: 15px; letter-spacing: 3px; margin-top: 8px; }
  .brand-tagline {
    position: absolute;
    left: 0; right: 0; top: 178px;
    font-family: "Cinzel", serif;
    font-size: 9px;
    letter-spacing: 2px;
    color: var(--leaf);
  }
  /* back */
  .holder-name {
    position: absolute;
    left: 62px; top: 48px;
    font-family: "Cinzel", serif;
    font-weight: 400;
    font-size: 24px;
    line-height: 30px;
    color: var(--leaf);
    letter-spacing: 0.5px;
  }
  .address {
    position: absolute;
    right: 280px; top: 190px;
    text-align: right;
    font-family: "Crimson Text", serif;
    font-style: normal;
    font-size: 13px;
    line-height: 18px;
    color: var(--muted);
  }
  .contact-list {
    position: absolute;
    left: 262px; top: 94px;
    list-style: none;
    font-family: "Crimson Text", serif;
    font-size: 13px;
    color: var(--muted);
  }
  .contact-list li {
    display: flex;
    align-items: center;
    gap: 7px;
    height: 21px;
  }
  .contact-list svg { width: 11px; height: 11px; flex: none; }
</style>
</head>
<body>

  <section class="card card--front" aria-label="Business card front">
    <h1 class="brand-name">
      <span class="brand-name__main">Silver Brook</span>
      <span class="brand-name__sub">Constructions Ltd.</span>
    </h1>
    <p class="brand-tagline">Building homes that endure</p>
  </section>

  <section class="card card--back" aria-label="Business card back">
    <h2 class="holder-name">Dalton Wexford</h2>

    <ul class="contact-list">
      <li>
        <svg viewBox="0 0 12 12" aria-hidden="true"><path d="M3 1 L5 3.5 L4 5 Q5.5 7 7 8 L8.5 7 L11 9 L9.5 11 Q4 10 1 2.5 Z" fill="var(--muted)"/></svg>
        250-384-6252
      </li>
      <li>
        <svg viewBox="0 0 12 12" aria-hidden="true"><rect x="3" y="1" width="6" height="4" fill="var(--muted)"/><rect x="1" y="5" width="10" height="4" rx="1" fill="var(--muted)"/><rect x="3" y="8" width="6" height="3" fill="var(--muted)"/></svg>
        222-222-2222
      </li>
      <li>
        <svg viewBox="0 0 12 12" aria-hidden="true"><circle cx="6" cy="6" r="5.5" fill="var(--leaf)"/><rect x="3" y="4" width="6" height="4" fill="#fff"/></svg>
        dalton@silverbrookconstructions.example
      </li>
      <li>
        <svg viewBox="0 0 12 12" aria-hidden="true"><circle cx="6" cy="6" r="5.5" fill="var(--muted)"/><circle cx="6" cy="6" r="3" fill="none" stroke="#fff" stroke-width="1"/></svg>
        www.silverbrookconstructions.example
      </li>
    </ul>

    <address class="address">
      4816 Ardmore Rd.<br>
      Victoria B.C. V8N 4K7
    </address>
  </section>

</body>
</html>
```